Pure Aurelle "polish the glow you hold" The whole body approach to beauty, customized skincare a

I need a stronger logo design than what I have now. I currently have a small med spa in Chicago, IL. I will be expanding my brand to New York City and the Hamptons of NY. The services I provide in Chicago include; advanced medical grade skincare treatments, laser, plastic surgery and nutrition counsel. My concept is personalized skincare. Part of my philosophy is to dedicate a lot of time and make myself always available to my clients questions and concerns. To maintain integrity of the Pure Aurelle Philosophy I do not advertise. Pure Aurelle is an "exclusive skincare club" therefore you must be referred by an existing client or staff member in order to get an appointment. My Chicago clientele consists of young professionals competing with their peers to look their absolute best. The New York and Hamptons business has a completely different structure. It is a Mobile med spa service providing treatments at people's homes. The services provided are advanced skincare, wellness, massage, spray tan, hair and makeup. My vision for the new logo design is to exude an image that is both cutting edge, relevant, sophisticated, sexy and modern (sleek) yet practical and strong. It must be eye catching yet simplistic, aesthetically pleasing to look at and above all must promote EXCLUSIVITY! bellow I have attached my current logo design which is printed using silver and gold foil. The other is the logo on my prescription skincare products. I need to merge the two for the brand to be cohesive. I would like to print my business cards on a mirror like material where you can see your reflection. Front of card: the brand Pure Aurelle across the front and across the bottom will be Chicago. New York. Hamptons Back of card: in a font style like writing "Pure Aurelle is the whole body approach to beauty. customized medical grade skincare. massage. wellness counsel. By appointment only
www.purenaurellecare.example p: (555) 318-2046
I am open to all suggestions to make my brand as strong as possible. Please be creative and relevant. Thank you!

```html
<!DOCTYPE html>
<html lang="en">
<head>
<meta charset="utf-8">
<title>Pure Aurelle – Business Card</title>
<link rel="stylesheet" href="https://fonts.googleapis.com/css2?family=Caveat:wght@400;500&family=Heebo:wght@200;300;400&display=swap">
<style>
  :root {
    --page: #ffffff;
    --mirror: #8fa8c4;
    --mirror-note: rgba(255, 255, 255, 0.38);
    --white: #ffffff;
    --navy: #1e5088;
    --teal: #73c8bc;
    --mint: #b0f5e2;
    --gold: #b19a50;
    --label: #8a9a9e;
    --crop: #222222;
    --sans: "Heebo", "Helvetica Neue", Arial, sans-serif;
    --script: "Caveat", "Comic Sans MS", cursive;
  }
  * { margin: 0; padding: 0; box-sizing: border-box; }
  html, body { width: 1114px; height: 1200px; overflow: hidden; background: var(--page); }
  .sheet { position: relative; width: 1114px; height: 1200px; font-family: var(--sans); }

  .card { position: absolute; top: 45px; width: 458px; height: 785px; }
  .card--front { left: 60px; background: var(--mirror); }
  .card--back { left: 585px; background: var(--white); border: 1px solid #f1f3f3; }

  .marks { position: absolute; inset: 0; width: 1114px; height: 1200px; pointer-events: none; }

  .mirror-note {
    position: absolute; width: 160px; margin-left: -80px; text-align: center;
    color: var(--mirror-note); font-weight: 300; font-size: 26px; line-height: 34px;
  }
  .mirror-note--x { width: 40px; margin-left: -20px; font-size: 36px; }

  .front-brand {
    position: absolute; left: 0; right: 0; top: 651px; text-align: center;
    color: var(--white); font-weight: 400; font-size: 50px; letter-spacing: -1.5px;
  }
  .front-cities {
    position: absolute; left: 0; right: 0; top: 718px; text-align: center;
    color: var(--white); font-weight: 300; font-size: 23px; letter-spacing: 0.5px;
  }

  .philosophy {
    position: absolute; left: 0; right: 0; top: 66px; text-align: center;
    color: var(--navy); font-family: var(--script); font-weight: 500;
    font-size: 47px; line-height: 49px;
  }
  .philosophy__name { display: block; font-size: 66px; line-height: 70px; }

  .appointment {
    position: absolute; left: 0; right: 0; top: 522px; text-align: center; color: var(--teal);
    font-weight: 200; font-size: 31px; letter-spacing: -0.5px;
  }
  .phone {
    position: absolute; left: 0; right: 0; top: 562px; text-align: center; color: var(--teal);
    font-weight: 300; font-size: 31px; letter-spacing: 2px;
  }
  .back-brand {
    position: absolute; left: 33px; top: 648px; color: var(--teal);
    font-weight: 400; font-size: 50px; letter-spacing: -1.5px;
  }
  .rule { position: absolute; left: 0; right: 0; top: 725px; height: 3px; display: flex; }
  .rule__gold { flex: 0 0 338px; background: var(--gold); }
  .rule__teal { flex: 1; background: var(--teal); }
  .website {
    position: absolute; left: 36px; top: 732px; color: var(--teal);
    font-weight: 300; font-size: 23px; letter-spacing: 1.5px;
  }

  .side-label {
    position: absolute; top: 868px; width: 458px; text-align: center;
    color: var(--label); font-weight: 300; font-size: 50px; letter-spacing: 3px;
  }
  .side-label--front { left: 60px; }
  .side-label--back { left: 585px; }

  .palette { position: absolute; left: 75px; top: 995px; }
  .palette__title { color: var(--label); font-weight: 300; font-size: 27px; letter-spacing: 1.5px; }
  .palette__swatches { display: flex; margin-top: 15px; }
  .swatch { width: 87px; height: 89px; }
  .swatch--gold { background: var(--gold); }
  .swatch--mint { background: var(--mint); }
  .swatch--teal { background: var(--teal); }
  .swatch--navy { background: var(--navy); }
</style>
</head>
<body>
<main class="sheet">

  <section class="card card--front" aria-label="Card front">
    <div class="mirror-note" style="left:233px; top:200px;">Mirror<br>Material</div>
    <div class="mirror-note" style="left:114px; top:352px;">Mirror<br>Material</div>
    <div class="mirror-note" style="left:344px; top:352px;">Mirror<br>Material</div>
    <div class="mirror-note mirror-note--x" style="left:230px; top:372px;">X</div>
    <div class="mirror-note" style="left:230px; top:472px;">Mirror<br>Material</div>
    <div class="front-brand">Pure Aurelle</div>
    <div class="front-cities">Chicago • New York • Hamptons</div>
  </section>

  <section class="card card--back" aria-label="Card back">
    <p class="philosophy">
      <span class="philosophy__name">Pure Aurelle</span>
      is the whole body<br>
      approach to beauty.<br>
      Customized medical<br>
      grade skincare.<br>
      Massage.<br>
      Wellness counsel.
    </p>
    <div class="appointment">By appointment only</div>
    <div class="phone">(555) 318-2046</div>
    <div class="back-brand">Pure Aurelle</div>
    <div class="rule"><span class="rule__gold"></span><span class="rule__teal"></span></div>
    <div class="website">www.purenaurellecare.example</div>
  </section>

  <svg class="marks" viewBox="0 0 742.67 800" aria-hidden="true">
    <g stroke="rgba(255,255,255,0.38)" stroke-width="1.4">
      <line x1="60" y1="65" x2="72" y2="85"/><line x1="87" y1="108" x2="98" y2="128"/>
      <line x1="110" y1="152" x2="122" y2="172"/><line x1="135" y1="195" x2="147" y2="215"/>
      <line x1="160" y1="240" x2="172" y2="260"/><line x1="212" y1="325" x2="225" y2="345"/>
      <line x1="235" y1="370" x2="247" y2="390"/><line x1="262" y1="415" x2="275" y2="435"/>
      <line x1="287" y1="458" x2="300" y2="478"/><line x1="312" y1="502" x2="325" y2="522"/>
      <line x1="325" y1="65" x2="313" y2="85"/><line x1="298" y1="108" x2="287" y2="128"/>
      <line x1="275" y1="152" x2="263" y2="172"/><line x1="250" y1="195" x2="238" y2="215"/>
      <line x1="225" y1="240" x2="213" y2="260"/><line x1="173" y1="325" x2="160" y2="345"/>
      <line x1="150" y1="370" x2="138" y2="390"/><line x1="123" y1="415" x2="110" y2="435"/>
      <line x1="98" y1="458" x2="85" y2="478"/><line x1="73" y1="502" x2="60" y2="522"/>
    </g>
    <g stroke="var(--crop)" stroke-width="0.9" fill="none">
      <path d="M26 30H56M40 16V46"/><path d="M330 30H360M345 16V46"/>
      <path d="M26 553H56M40 539V569"/><path d="M330 553H360M345 539V569"/>
      <path d="M375 30H405M390 16V46"/><path d="M680 30H710M695 16V46"/>
      <path d="M375 553H405M390 539V569"/><path d="M680 553H710M695 539V569"/>
    </g>
  </svg>

  <div class="side-label side-label--front">FRONT</div>
  <div class="side-label side-label--back">BACK</div>

  <section class="palette" aria-label="Colour palette">
    <div class="palette__title">COLOR PALETTE</div>
    <div class="palette__swatches">
      <span class="swatch swatch--gold"></span>
      <span class="swatch swatch--mint"></span>
      <span class="swatch swatch--teal"></span>
      <span class="swatch swatch--navy"></span>
    </div>
  </section>

</main>
</body>
</html>
```